Flyer-Design für ein Ingenieur- und Planungsbüro
Ein toller Entwurf und freundliche Kommunikation inkl. immer schneller Reaktionszeit, auch wenn es bei mir manchmal mit der Zuarbeit der passenden Bilder gedauert hat. Perfektes Ergebnis!!
Zielgruppe
Ingenieur- und Planungsbüro (Dienstleister) aus Leipzig, welches seit 22 Jahren auf die Optimierung und Neuerrichtung
medizinischer Einrichtungen (Arzt- und Zahnarztpraxen) spezialisiert ist.
Zur Zielgruppe zählen daher Mediziner und Zahnmedizinen zwischen 30 - 55 Jahren, welche bereits eine Praxis führen oder gerade neu gründen möchten. Die Schnittmenge liegt im Praxisstandort = Praxisräume, welche niedergelassene Mediziner zur Ausübung ihrer Tätigkeiten inkl. Personal, Medizintechnik und sonstige Ausstattung benötigen. Der Verkauf von Produkten und Einrichtungen ist nicht meine Aufgabe.
Meine Tätigkeiten liegen in der Beratung, Unterstützung der Medizinerinnen über das gesamte Projekt, von der ersten Idee, über die Umsetzung bis zur Praxiseröffnung. Ich bin daher Lotse, Koordinator aller Projektschnittstellen sowie Planer zur Umsetzung der jeweiligen Kundenanforderungen. Die Leistungsdetails und Stichpunkte sind den Unterlagen zu entnehmen oder weiter zu erfragen.
Aufgabenstellung
Der Flyer soll nach einem telefonischen Erstkontakt oder nach einem persönlichen Treffen meinen potenziellen Kunden einen Überblick zu den Umfangreichen Leistungsportfolio geben. Der Flyer soll professionell und seriös wirken und meine langjährige Expertise und Knowhow vermitteln.
Weiterhin soll der Flyer meinen Netzwerkpartner dienen, welche ebenfalls mit der Zielgruppe der Heilberufe im geschäftlichen Kontakt sind und mich über den Flyer im Gespräch weiterempfehlen und zu einem Neukontakt zwischen dem potenziellen Kunden/ Kundin führen soll.
Der in den Daten zur Verfügung gestellt Entwurf des Flyers braucht nicht 1:1 nachgebaut werden. Er bietet vielmehr eine Orientierung wie ich mir einen Flyer vorstellen kann. Auch die zur Verfügung gestellten Bilden dienen zur Orientierung, ggf. werden diese nach Feststellung des Siegers/ Siegerin im Detail nochmals angepasst.
Farben:
Blau: 041-171-226 / #29abe2
Grün: 140-198-063 / #8cc63f

```html
<!DOCTYPE html>
<html lang="de">
<head>
<meta charset="utf-8">
<title>Praxiswerk Lotsen UG – Faltflyer</title>
<link rel="stylesheet" href="https://fonts.googleapis.com/css2?family=Montserrat:wght@300;400;500;700;800&display=swap">
<style>
:root{
  --blue:#4f67a3;
  --blue-dark:#45598f;
  --green:#a6c02c;
  --green-dark:#8fa824;
  --text:#555a60;
  --paper:#f4f4f4;
  --paper-grey:#dcdcdc;
  --stage:#e8e8e8;
  --white:#ffffff;
}
*{margin:0;padding:0;box-sizing:border-box}
html,body{width:1200px;height:749px;overflow:hidden;background:var(--stage);font-family:"Montserrat",Arial,sans-serif;color:var(--text)}
.panel{position:absolute;top:120px;width:245px;height:510px;overflow:hidden;background:var(--paper)}
.panel svg.shapes{position:absolute;inset:0}
.photo{position:absolute}
.cover{left:50px}
.inside-about{left:360px;background:var(--paper-grey)}
.inside-modules{left:605px}
.inside-service{left:850px}

.brand{position:absolute;display:flex;align-items:flex-start;gap:6px;font-weight:300;color:#7b8088;line-height:1.05}
.brand-mark{width:10px;height:10px;background:var(--blue);margin-top:4px;flex:none}

.headline{position:absolute;left:23px;top:340px;font-weight:800;color:var(--blue);font-size:27px;line-height:33px;letter-spacing:.2px}
.headline span{display:block;position:relative}
.headline span+span::before{content:"";position:absolute;left:0;top:-3px;width:22px;height:2px;background:var(--green)}
.headline span.last::after{content:"";position:absolute;left:0;bottom:-2px;width:22px;height:2px;background:var(--green)}
.tagline{position:absolute;left:23px;top:460px;font-size:10.5px;letter-spacing:.3px;color:#555}

h2{font-weight:800;color:var(--blue);letter-spacing:.3px}
.about-title{position:absolute;left:22px;top:18px;font-size:16px}
.portrait{position:absolute;left:0;top:42px;width:80px;height:54px}
.about-intro{position:absolute;left:22px;top:43px;width:206px;font-size:7.6px;line-height:11.6px}
.about-intro b{font-weight:700}
.about-intro .indent{display:block;padding-left:63px}
.check{display:inline-block;width:8px;height:8px;background:var(--green);margin-right:4px;vertical-align:-1px;position:relative}
.check::after{content:"";position:absolute;left:2px;top:2px;width:3px;height:3px;border-right:1px solid #fff;border-top:1px solid #fff;transform:rotate(45deg)}
.about-point{position:absolute;left:22px;width:200px;font-size:7.6px;line-height:11.6px}

.modules-box{position:absolute;left:16px;top:325px;width:220px;color:#fff}
.modules-box h2{color:#fff;font-size:14.5px;margin-bottom:8px}
.list{list-style:none}
.list li{position:relative;padding-left:11px;font-size:7.6px;line-height:11px;margin-bottom:6px}
.list li::before{content:"";position:absolute;left:0;top:2px;width:6px;height:6px;background:rgba(255,255,255,.85)}
.service-box{position:absolute;left:22px;top:55px;width:212px}
.service-box h2{font-size:16px;margin-bottom:6px}
.service-box .list li{font-size:8px;line-height:11.5px;margin-bottom:7px;color:#444}
.service-box .list li::before{background:var(--green)}
</style>
</head>
<body>

<!-- Titelseite -->
<section class="panel cover">
  <div class="photo" role="img" aria-label="Foto eines hellen Zahnarzt-Behandlungsraums mit Behandlungsstuhl" style="left:0;top:0;width:245px;height:230px;background:linear-gradient(135deg,#f1efec 0%,#dedad4 45%,#b8b4ae 75%,#5d6064 100%)"></div>
  <svg class="shapes" width="245" height="510" viewBox="0 0 245 510">
    <polyline points="0,20 230,20 230,245" fill="none" stroke="#fff" stroke-width="3"/>
    <polygon points="0,200 100,200 135,250 245,250 245,510 0,510" fill="var(--paper)"/>
    <polygon points="135,230 172,230 150,275 113,275" fill="var(--green)"/>
    <polygon points="150,240 245,237 245,285 118,287" fill="var(--blue)"/>
    <polygon points="170,500 180,485 245,485 245,510 165,510" fill="var(--green)"/>
  </svg>
  <div class="brand" style="left:16px;top:215px;font-size:17px">
    <span class="brand-mark"></span><span>Praxiswerk<br>Lotsen UG</span>
  </div>
  <h1 class="headline"><span>KONZEPTION</span><span>PLANUNG</span><span class="last">UMSETZUNG</span></h1>
  <p class="tagline">EXPERTISE, KNOWHOW, ÜBERSICHT</p>
</section>

<!-- Innenseite 1: Über -->
<section class="panel inside-about">
  <h2 class="about-title">UBER</h2>
  <div class="portrait" role="img" aria-label="Porträtfoto des Geschäftsführers" style="background:linear-gradient(90deg,#6d7480,#3c4250)"></div>
  <p class="about-intro"><span class="indent"><b>Jonas Feldmeier</b>, Geschäftsführer der Praxiswerk Lotsen UG. Industriemeister, Baufachwirt, Betriebswirt (IHK). Seit 22 Jahren spezialisiert auf ambulante</span>Einrichtungen des Gesundheitswesens.</p>
  <p class="about-point" style="top:125px"><span class="check"></span>Ihr übergreifender Spezialist für alle Schnittstellen und Projektetappen. Professionelle Unterstützung und Lotse für alle Heilberufe rund um Ihren Praxisstandort.</p>
  <p class="about-point" style="top:185px"><span class="check"></span>Für Neugründung, Bestandsoptimierung und Standortsuche. Von der Idee bis zur Praxis -Neueröffnung.</p>
  <div class="photo" role="img" aria-label="Foto einer Baustelle im Innenausbau mit Fenstern und Dämmmaterial" style="left:0;top:240px;width:245px;height:270px;background:linear-gradient(160deg,#7f7a74 0%,#b7b5b0 40%,#d8d4cc 60%,#8e9296 100%)"></div>
  <svg class="shapes" width="245" height="510" viewBox="0 0 245 510">
    <polygon points="210,240 245,240 245,510 150,510 245,300 245,300" fill="var(--paper-grey)"/>
    <polygon points="245,300 245,510 150,510" fill="var(--green-dark)"/>
    <polygon points="210,240 245,240 245,300 245,310" fill="var(--paper-grey)"/>
    <polygon points="120,220 160,220 190,268 150,268" fill="var(--green)"/>
    <polygon points="175,228 210,228 228,262 193,262" fill="var(--blue)"/>
  </svg>
</section>

<!-- Innenseite 2: Leistungsbausteine -->
<section class="panel inside-modules">
  <div class="photo" role="img" aria-label="Foto eines leeren Rohbau-Büroraums mit Fensterfront" style="left:0;top:0;width:245px;height:300px;background:linear-gradient(180deg,#9c9891 0%,#c9c6c0 40%,#9a958d 75%,#6f6a62 100%)"></div>
  <svg class="shapes" width="245" height="510" viewBox="0 0 245 510">
    <polyline points="0,15 228,15 228,300" fill="none" stroke="#fff" stroke-width="3"/>
    <polygon points="0,205 100,205 130,245 245,245 245,300 0,300" fill="var(--paper)"/>
    <polygon points="100,235 135,235 105,280 70,280" fill="var(--green)"/>
    <polygon points="125,242 245,242 245,285 108,287" fill="var(--blue)"/>
    <rect x="0" y="297" width="245" height="213" fill="var(--green)"/>
    <polygon points="245,440 245,510 210,510" fill="var(--paper)"/>
  </svg>
  <div class="brand" style="left:18px;top:222px;font-size:13px">
    <span class="brand-mark" style="width:8px;height:8px;margin-top:3px"></span><span>Praxiswerk<br>Lotsen UG</span>
  </div>
  <div class="modules-box">
    <h2>LEISTUNGSBAUSTEINE:</h2>
    <ul class="list">
      <li>Standortsuche, Bewertung, Machbarkeitsprüfung</li>
      <li>Konzeption, Funktionsplanung, Kostenschätzung</li>
      <li>Projektplanung, Terminplanung, Ausbaubeschreibung</li>
      <li>Entwurfs-, Einrichtungs- und Ausführungsplanung</li>
      <li>Ausschreibungen, Leistungsvergabe, Schnittstellenmanagement</li>
      <li>Projekt- und Bauüberwachung, bis zur Praxiseröffnung</li>
    </ul>
  </div>
</section>

<!-- Innenseite 3: Service -->
<section class="panel inside-service">
  <div class="photo" role="img" aria-label="Foto eines Praxis-Sterilisationsraums mit weißen Schränken und Spüle" style="left:0;top:240px;width:245px;height:205px;background:linear-gradient(135deg,#e9e9ea 0%,#cfd1d4 50%,#8fa2c0 80%,#6d84b0 100%)"></div>
  <svg class="shapes" width="245" height="510" viewBox="0 0 245 510">
    <polygon points="210,0 245,0 245,60" fill="var(--green)"/>
    <polygon points="0,230 245,230 245,240 0,250" fill="var(--paper)"/>
    <polygon points="115,220 160,220 185,262 140,262" fill="var(--green)"/>
    <polygon points="168,228 205,228 228,262 191,262" fill="var(--blue)"/>
    <polygon points="0,440 245,432 245,445 0,455" fill="var(--paper)"/>
    <polygon points="15,460 245,455 245,510 0,510" fill="var(--blue)"/>
  </svg>
  <div class="service-box">
    <h2>SERVICE:</h2>
    <ul class="list">
      <li>unabhängige Leistungen, kein Produktverkauf</li>
      <li>Steuerung und Koordination von Gewerken, Dienstleistern und Technikern</li>
      <li>Management Dritter am Projekt Beteiligter (Vermieter, Bauträger, Dental-/ Medizintechnik, IT, Einrichtung, uvm.)</li>
      <li>volle Kosten und Terminkontrolle</li>
      <li>bedarfsgerechte und flexible Beratung, Unterstützung, Planung</li>
    </ul>
  </div>
</section>

</body>
</html>
```